Kessler MD Summit Primary Care Business Card

Need a business card for a medical clinic targeting VIP patients. Should portray an upscale feeling. Simple, clean design. Logo and colors need to be incorporated into card. Clinic colors are gray/ silver, blues, white same as logo.
Clinic is a cash only VIP service clinic targeting higher income patients.
Tagline: "Where each visit is unhurried - Care Made Personal"

Target Market(s)

VIP, upscale

Industry/Entity Type

Medical

Contact Information for Business Card

Would like to use for cards with raised print or metallic highlight.

Requirements
Must have
• Incorporate logo, Use colors in logo
Nice to have
• Metallic detail
Should not have
• too much details or colors, other stock photos or designs

```html
<!DOCTYPE html>
<html lang="en">
<head>
<meta charset="utf-8">
<title>Kessler MD Summit Primary Care – Business Card</title>
<link rel="stylesheet" href="https://fonts.googleapis.com/css2?family=Cinzel:wght@400;600&display=swap">
<style>
  :root {
    --navy: #2c4059;
    --silver: #9ea3a3;
    --ink: #4a5058;
    --paper: #ffffff;
    --paper-soft: #f3f4f4;
    --backdrop: #e6e7e8;
  }
  * { box-sizing: border-box; margin: 0; padding: 0; }
  html, body {
    width: 1200px; height: 800px; overflow: hidden;
    background: var(--backdrop);
    font-family: "Cinzel", Georgia, serif;
  }
  .sheet {
    width: 1200px; height: 800px;
    display: flex; align-items: center; justify-content: center; gap: 40px;
  }
  .card {
    width: 540px; height: 310px;
    background: var(--paper);
    box-shadow: 0 2px 6px rgba(0,0,0,.12);
  }

  /* Front */
  .card--front { padding: 16px; }
  .front__field {
    width: 100%; height: 100%;
    background: var(--navy);
    display: flex; flex-direction: column; align-items: center; justify-content: center;
    gap: 14px;
  }
  .brand-dot {
    width: 46px; height: 46px; border-radius: 50%;
    background: var(--silver);
  }
  .brand-name {
    text-align: center; color: var(--paper);
    font-weight: 400; letter-spacing: 1px; line-height: 1.3;
  }
  .front__field .brand-name { font-size: 24px; }

  /* Back */
  .card--back { padding: 12px; background: var(--paper-soft); }
  .back__frame {
    width: 100%; height: 100%;
    border: 2px solid var(--navy);
    background: var(--navy);
  }
  .back__panel {
    width: 100%; height: 100%;
    background: var(--paper-soft);
    border-radius: 0 80px 0 80px;
    display: grid;
    grid-template-columns: 1fr 1fr;
    grid-template-rows: 1fr auto;
    padding: 30px 24px 20px;
  }
  .back__brand {
    display: flex; flex-direction: column; align-items: center; justify-content: center; gap: 12px;
  }
  .back__brand .brand-dot { width: 40px; height: 40px; }
  .back__brand .brand-name { color: var(--navy); font-size: 17px; }
  .contact { color: var(--ink); padding-left: 20px; padding-top: 12px; }
  .contact__name { color: var(--navy); font-size: 20px; font-weight: 600; letter-spacing: 1px; margin-bottom: 14px; }
  .contact__lines { font-size: 11.5px; line-height: 1.35; letter-spacing: .5px; list-style: none; }
  .contact__lines .gap { margin-top: 12px; }
  .tagline {
    grid-column: 1 / -1; text-align: center;
    color: var(--ink); font-size: 12.5px; letter-spacing: .6px;
  }
</style>
</head>
<body>
<main class="sheet">
  <section class="card card--front" aria-label="Card front">
    <div class="front__field">
      <span class="brand-dot"></span>
      <p class="brand-name">Kessler MD<br>Summit Primary Care</p>
    </div>
  </section>

  <section class="card card--back" aria-label="Card back">
    <div class="back__frame">
      <div class="back__panel">
        <div class="back__brand">
          <span class="brand-dot"></span>
          <p class="brand-name">Kessler MD<br>Summit Primary Care</p>
        </div>
        <div class="contact">
          <h1 class="contact__name">Kessler MD</h1>
          <ul class="contact__lines">
            <li>PO Box 456 Maplewood</li>
            <li>NY 12987</li>
            <li class="gap">555-210-447</li>
            <li>hello@kesslermd.com</li>
            <li>www.kesslermd.com</li>
          </ul>
        </div>
        <p class="tagline">Where each visit is unhurried - Care Made Personal</p>
      </div>
    </div>
  </section>
</main>
</body>
</html>
```